Buchcover-Design für Science-Fiction-Roman
Zielgruppe
Ich habe einen Science-Fiction-Roman geschrieben und benötige dafür ein Buchcover.
Meine Zielgruppe sind Leser- und Leserinnen ab 18, Science-Fiction-Fans.
Aufgabenstellung
Zur Einstimmung und Orientierung habe ich ein kurzes Exposé und eine Leseprobe des Romans hochgeladen.
Für das Cover stelle ich mir etwas Dezentes aber trotzdem künstlerisch Anspruchsvolles vor, gerne auch abstrakt.
Es sollte der Titel (Unter Glas), meine Name (Lenor Vasić) und 'Roman' auf dem Cover.
Den genauen Klappentext reiche ich noch nach.
Das Format ist 12,7 x 20,32 cm (5 x 8 Zoll), Rückenbreite etwa 2 cm.

```html
<!DOCTYPE html>
<html lang="de">
<head>
<meta charset="utf-8">
<title>Unter Glas – Buchumschlag</title>
<link rel="stylesheet" href="https://fonts.googleapis.com/css2?family=Anton&family=Barlow:wght@400;500&display=swap">
<style>
  :root {
    --page-bg: #ffffff;
    --back-top: #e5bf40;
    --back-bottom: #a8691a;
    --spine: #612a12;
    --spine-text: #e8c23a;
    --title-rust: #963c12;
    --title-brown: #5c2a10;
    --body-text: #5a2a0e;
    --front-top: #a86c1a;
    --front-mid: #e3ac1c;
    --front-bottom: #c08a22;
  }
  * { margin: 0; padding: 0; box-sizing: border-box; }
  html, body {
    width: 1200px; height: 889px; overflow: hidden;
    background: var(--page-bg);
  }
  .spread {
    position: absolute; left: 47px; top: 32px;
    width: 1106px; height: 820px;
  }
  .back-cover {
    position: absolute; left: 0; top: 0; width: 513px; height: 820px;
    background: linear-gradient(to bottom, var(--back-top), var(--back-bottom));
  }
  .title {
    font-family: "Anton", "Impact", sans-serif;
    font-weight: 400;
    text-transform: uppercase; line-height: 1; white-space: nowrap;
  }
  .back-cover .title-top {
    position: absolute; left: 47px; top: 55px;
    font-size: 94px; color: var(--title-rust);
  }
  .back-cover .title-bottom {
    position: absolute; left: 47px; top: 161px;
    font-size: 94px; color: var(--title-brown);
  }
  .blurb {
    position: absolute; left: 47px; top: 268px; width: 425px;
    font-family: "Barlow", sans-serif; font-size: 14.6px; line-height: 18.8px;
    color: var(--body-text);
  }
  .barcode-space {
    position: absolute; left: 271px; top: 663px; width: 202px; height: 122px;
    background: #ffffff;
  }
  .spine {
    position: absolute; left: 513px; top: 0; width: 81px; height: 820px;
    background: var(--spine);
  }
  .spine-text {
    position: absolute; left: 50%; white-space: nowrap;
    font-family: "Barlow", sans-serif; font-weight: 500; font-size: 26px;
    line-height: 32px;
    color: var(--spine-text);
    transform: translateX(-50%) rotate(-90deg);
  }
  .spine-title { top: 116px; }
  .spine-author { top: 690px; }
  .front-cover {
    position: absolute; left: 594px; top: 0; width: 512px; height: 820px;
    overflow: hidden;
  }
  .front-art {
    position: absolute; inset: 0;
    background:
      radial-gradient(ellipse at 60% 45%, rgba(245,200,60,0.7), transparent 60%),
      linear-gradient(to bottom, var(--front-top) 0%, var(--front-mid) 40%, var(--front-mid) 65%, var(--front-bottom) 100%);
  }
  .front-author {
    position: absolute; left: 168px; top: 65px;
    font-family: "Barlow", sans-serif; font-weight: 500; font-size: 27px;
    color: var(--title-brown);
  }
  .front-cover .title-top {
    position: absolute; left: 170px; top: 101px;
    font-size: 128px; color: var(--title-rust);
  }
  .front-cover .title-vertical {
    position: absolute; left: 347px; top: 265px;
    font-size: 200px; color: var(--title-brown);
    transform-origin: 0 0; transform: rotate(90deg);
    letter-spacing: 40px;
  }
</style>
</head>
<body>
  <div class="spread">
    <section class="back-cover">
      <h2 class="title title-top">Unter</h2>
      <h2 class="title title-bottom">Glas</h2>
      <p class="blurb">Lorem ipsum dolor sit amet, consectetuer adipiscing elit. Aenean commodo ligula eget dolor. Aenean massa. Cum sociis natoque penatibus et magnis dis parturient montes, nascetur ridiculus mus. Donec quam felis, ultricies nec, pellentesque eu, pretium quis, sem. Nulla consequat massa quis enim. Donec pede justo, fringilla vel, aliquet nec, vulputate eget, arcu. In enim justo, rhoncus ut, imperdiet a, venenatis vitae, justo. Nullam dictum felis eu pede mollis pretium. Integer tincidunt. Cras dapibus. Vivamus elementum semper nisi. Aenean vulputate eleifend tellus. Aenean leo ligula, porttitor eu, consequat vitae, eleifend ac, enim. Aliquam lorem ante, dapibus in, viverra quis, feugiat a, tellus.</p>
      <div class="barcode-space"></div>
    </section>
    <section class="spine">
      <span class="spine-text spine-title">Unter Glas</span>
      <span class="spine-text spine-author">Lenor Vasić</span>
    </section>
    <section class="front-cover">
      <div class="front-art" role="img" aria-label="Illustration: goldgelbe Skyline aus Hochhäusern im Dunst, eine Silhouette stürzt kopfüber herab"></div>
      <p class="front-author">Lenor Vasić</p>
      <h1 class="title title-top">Unter</h1>
      <p class="title title-vertical">Glas</p>
    </section>
  </div>
</body>
</html>
```